A5 size flyer for IT Company doing platform migrations

I need an A5 sized flyer for an IT company who specialise in platform migrations i.e. from one platform such as Pellora Deskline to another platform such as Tandem 480. The colours should be inline with what has been used in the attached logo file. The flyer is to be used in business shows that we attend and should be professional looking, be brief and to the point. The artwork should be IT platform migration related.

Target Market(s)

Other businesses

Colors
0054AA
0677BA
7BADD7
CADEEF
E8F1F8

```html
<!DOCTYPE html>
<html lang="en">
<head>
<meta charset="utf-8">
<title>Northvane IT Ltd – Platform Migration Flyer</title>
<link rel="stylesheet" href="https://fonts.googleapis.com/css2?family=Poppins:wght@400;500;600;700;800&display=swap">
<style>
  :root {
    --navy: #0054AA;
    --mid-blue: #0677BA;
    --sky: #7BADD7;
    --pale: #CADEEF;
    --mist: #E8F1F8;
    --accent: #1e9be0;
    --ink: #1b1b1b;
    --white: #ffffff;
  }
  * { margin: 0; padding: 0; box-sizing: border-box; }
  html, body { width: 839px; height: 1200px; overflow: hidden; background: #fff; }
  .flyer {
    position: relative;
    width: 839px;
    height: 1200px;
    overflow: hidden;
    font-family: "Poppins", Arial, sans-serif;
    background: linear-gradient(180deg, #ffffff 0%, #ffffff 45%, #eef0f3 75%, #e3e6ea 100%);
  }
  .header-wave, .footer-wave { position: absolute; left: 0; width: 839px; }
  .header-wave { top: 0; height: 260px; }
  .footer-wave { top: 1030px; height: 170px; }

  .heading {
    position: absolute;
    left: 34px;
    top: 14px;
    font-size: 68px;
    font-weight: 800;
    letter-spacing: 1px;
    color: var(--white);
    line-height: 1;
  }
  .hero-photo {
    position: absolute;
    left: 520px;
    top: -5px;
    width: 340px;
    height: 340px;
    border-radius: 50%;
    border: 10px solid var(--white);
    background: radial-gradient(circle at 40% 60%, #f4f6f8 0%, #d7dde3 45%, #8e99a6 80%, #4f5b68 100%);
  }
  .brand {
    position: absolute;
    left: 0;
    width: 839px;
    top: 250px;
    text-align: center;
  }
  .brand-name {
    font-size: 27px;
    font-weight: 500;
    color: var(--navy);
    letter-spacing: 1px;
  }
  .brand-tagline {
    font-size: 8px;
    color: var(--mid-blue);
    letter-spacing: 0.5px;
    margin-top: -2px;
  }
  .intro {
    position: absolute;
    left: 34px;
    top: 326px;
    width: 670px;
    font-size: 14.5px;
    line-height: 23px;
    font-weight: 600;
    color: var(--navy);
  }
  .skyline {
    position: absolute;
    left: 0;
    top: 810px;
    width: 839px;
    height: 300px;
    background: linear-gradient(180deg, rgba(200,205,212,0) 0%, rgba(170,177,186,0.55) 45%, rgba(140,148,158,0.75) 100%);
  }
  .body-copy {
    position: absolute;
    left: 34px;
    top: 480px;
    width: 310px;
    font-size: 13.5px;
    line-height: 21.6px;
    color: var(--ink);
  }
  .info-column {
    position: absolute;
    left: 490px;
    top: 570px;
    width: 320px;
  }
  .info-block { margin-bottom: 22px; }
  .info-title {
    font-size: 17px;
    font-weight: 600;
    color: var(--accent);
    margin-bottom: 4px;
  }
  .info-text {
    font-size: 13.5px;
    line-height: 21.6px;
    color: var(--ink);
  }
  .contact-bar {
    position: absolute;
    left: 0;
    top: 1110px;
    width: 839px;
    height: 90px;
    display: flex;
  }
  .contact-item {
    color: var(--white);
    font-size: 19px;
    font-weight: 700;
    line-height: 25px;
    padding-top: 22px;
  }
  .contact-item.address { width: 330px; padding-left: 90px; border-right: 2px solid var(--white); }
  .contact-item.phone { width: 270px; padding-left: 56px; border-right: 2px solid var(--white); }
  .contact-item.email { padding-left: 86px; }
</style>
</head>
<body>
<div class="flyer">
  <svg class="header-wave" viewBox="0 0 839 260" aria-hidden="true">
    <path d="M0 0 H839 V80 C720 78 640 95 570 120 C470 158 380 200 260 192 C160 185 80 140 0 142 Z" fill="var(--sky)"/>
    <path d="M0 0 H839 V66 C720 64 640 80 565 104 C465 142 375 182 260 176 C160 170 80 124 0 126 Z" fill="var(--mid-blue)"/>
    <path d="M0 0 H839 V56 C720 54 640 68 560 92 C460 128 375 168 260 162 C160 157 80 112 0 114 Z" fill="var(--navy)"/>
  </svg>

  <h1 class="heading">HEADING</h1>

  <div class="hero-photo" role="img" aria-label="Photo of a hand writing in a notebook beside a laptop keyboard"></div>

  <div class="brand">
    <div class="brand-name">NORTHVANE IT LTD</div>
    <div class="brand-tagline">PLATFORM MIGRATION SPECIALISTS</div>
  </div>

  <p class="intro">Lorem ipsum dolor sit amet, consectetur adipiscing elit, sed do eiusmod tempor incididunt ut labore et dolore magna aliqua. Ut enim ad minim veniam, quis nostrud exercitation ullamco laboris nisi ut aliquip ex ea commodo consequat. Duis aute irure dolor in reprehenderit in voluptate velit esse cillum dolore eu fugiat nulla pariatur. Excepteur sint occaecat cupidatat non proident, sunt in culpa qui officia deserunt mollit anim id est laborum.</p>

  <div class="skyline" role="img" aria-label="Faded city skyline with business people walking"></div>

  <p class="body-copy">Sed ut perspiciatis unde omnis iste natus error sit voluptatem accusantium doloremque laudantium, totam rem aperiam, eaque ipsa quae ab illo inventore veritatis et quasi architecto beatae vitae dicta sunt explicabo. Nemo enim ipsam voluptatem quia voluptas sit aspernatur aut odit aut fugit, sed quia consequuntur magni dolores eos qui ratione voluptatem sequi nesciunt. Neque porro quisquam est, qui dolorem ipsum quia dolor sit amet, consectetur, adipisci velit, sed quia non numquam eius modi tempora incidunt ut labore et dolore magnam aliquam quaerat voluptatem. Ut enim ad minima veniam, quis nostrum exercitationem ullam corporis suscipit laboriosam, nisi ut aliquid ex ea commodi consequatur? Quis autem vel eum iure reprehenderit qui in ea voluptate velit esse quam nihil molestiae consequatur, vel illum qui dolorem eum fugiat quo voluptas nulla pariatur.</p>

  <div class="info-column">
    <section class="info-block">
      <h2 class="info-title">WHO WE ARE</h2>
      <p class="info-text">Sed ut perspiciatis unde omnis istenatus error sit voluptatem accusantium doloremque laudantium, totam rem aperiam, eaque ipsa quae ab illo inventore</p>
    </section>
    <section class="info-block">
      <h2 class="info-title">OUR MISSION</h2>
      <p class="info-text">Sed ut perspiciatis unde omnis istenatus error sit voluptatem accusantium doloremque laudantium, totam rem aperiam, eaque ipsa quae ab illo inventore</p>
    </section>
    <section class="info-block">
      <h2 class="info-title">OUR VISION</h2>
      <p class="info-text">Sed ut perspiciatis unde omnis istenatus error sit voluptatem accusantium doloremque laudantium, totam rem aperiam, eaque ipsa quae ab illo inventore</p>
    </section>
  </div>

  <svg class="footer-wave" viewBox="0 0 839 170" aria-hidden="true">
    <path d="M0 52 C150 22 260 70 420 58 C560 46 700 14 839 30 V170 H0 Z" fill="var(--sky)"/>
    <path d="M0 64 C150 36 260 82 420 70 C560 58 700 28 839 42 V170 H0 Z" fill="var(--mid-blue)"/>
    <path d="M0 76 C150 50 260 94 420 82 C560 70 700 42 839 56 V170 H0 Z" fill="var(--navy)"/>
  </svg>

  <div class="contact-bar">
    <div class="contact-item address">ADDRESS :</div>
    <div class="contact-item phone">PHONE<br>NUMBER :</div>
    <div class="contact-item email">EMAIL :</div>
  </div>
</div>
</body>
</html>
```